Quiet Under Glass

Creation of a cover for a detective story
Size: 14 x 20.5 cm
Title: Quiet Under Glass
Author: Bastien Marchetaud
Publisher (at the bottom of the page): Editions Brunelle
Abstract: A surgeon in a hospital is faced with a series of post-operative infections. He suspects foul play due to the ongoing hostility of one of his colleagues.
Suggested Visual Elements:
- Hospital
- Operative room, with a surgeon and an African anesthetic
- Beautiful woman of 40 years old.
Target Market(s)
Adults
Industry/Entity Type
Book
Look and feel
Each slider illustrates characteristics of the customer's brand and the style your logo design should communicate.

```html
<!DOCTYPE html>
<html lang="en">
<head>
<meta charset="utf-8">
<title>Quiet Under Glass — Cover Spread</title>
<link rel="stylesheet" href="https://fonts.googleapis.com/css2?family=Bodoni+Moda:wght@400;500&family=Montserrat:wght@400;500;600&display=swap">
<style>
  :root {
    --page-bg: #ffffff;
    --back-bg: #000000;
    --front-bg: #0b0e1b;
    --spine-bg: #0a0d19;
    --ink-light: #ffffff;
    --accent-red: #ec1c1f;
    --serif: "Bodoni Moda", "Didot", serif;
    --sans: "Montserrat", "Helvetica Neue", sans-serif;
  }
  * { box-sizing: border-box; margin: 0; padding: 0; }
  html, body {
    width: 1200px; height: 1200px; overflow: hidden;
    background: var(--page-bg);
  }
  .spread {
    position: absolute; left: 50px; top: 205px;
    width: 1100px; height: 790px;
    display: flex;
  }
  /* Back cover */
  .back-cover {
    width: 528px; height: 100%;
    background: var(--back-bg);
    color: var(--ink-light);
    padding: 108px 0 0 66px;
    overflow: hidden;
  }
  .back-title {
    display: block;
    width: 396px; height: 44px;
    margin-bottom: 18px;
  }
  .back-title text {
    font-family: var(--serif);
    font-weight: 400;
    font-size: 40px;
  }
  .blurb {
    width: 395px;
    font-family: var(--sans);
    font-size: 12.6px;
    line-height: 19.8px;
    text-align: justify;
  }
  .blurb + .blurb { margin-top: 19.8px; }
  /* Spine */
  .spine {
    width: 45px; height: 100%;
    background: var(--spine-bg);
    overflow: hidden;
  }
  .spine-text { display: block; width: 45px; height: 790px; }
  .spine-title { font-family: var(--serif); font-size: 32px; }
  .spine-author { font-family: var(--serif); font-size: 18px; }
  .spine-publisher { font-family: var(--sans); font-weight: 600; font-size: 9px; }
  /* Front cover */
  .front-cover {
    position: relative;
    width: 527px; height: 100%;
    background: var(--front-bg);
    overflow: hidden;
  }
  .cover-photo {
    position: absolute; inset: 0 0 170px 0;
    background:
      radial-gradient(ellipse 90px 160px at 272px 170px, rgba(255,244,226,0.95), rgba(220,200,170,0.55) 45%, rgba(60,80,120,0) 100%),
      radial-gradient(ellipse 240px 380px at 270px 240px, rgba(70,95,140,0.55), rgba(11,14,27,0) 100%),
      linear-gradient(180deg, #1a2238 0%, #121a2e 55%, var(--front-bg) 100%);
  }
  .front-title {
    position: absolute; left: 0; top: 0;
    width: 527px; height: 640px;
  }
  .front-title text {
    font-family: var(--serif);
    font-weight: 400;
    font-size: 185px;
  }
  .author {
    position: absolute; left: 0; right: 0; top: 693px;
    text-align: center;
    font-family: var(--serif);
    font-size: 24px;
    letter-spacing: 0.2em;
    color: var(--ink-light);
    text-transform: uppercase;
  }
  .publisher {
    position: absolute; left: 0; right: 0; top: 740px;
    text-align: center;
    font-family: var(--sans);
    font-weight: 600;
    font-size: 10px;
    letter-spacing: 0.08em;
    color: var(--ink-light);
    text-transform: uppercase;
  }
</style>
</head>
<body>
  <main class="spread">
    <section class="back-cover">
      <svg class="back-title" viewBox="0 0 396 44" aria-label="Quiet Under Glass">
        <text x="0" y="38" fill="var(--ink-light)" textLength="300" lengthAdjust="spacingAndGlyphs">QUIET UNDER</text>
        <text x="314" y="38" fill="var(--accent-red)" textLength="82" lengthAdjust="spacingAndGlyphs">GLASS</text>
      </svg>
      <p class="blurb">Lorem ipsum dolor sit amet, consectetur adipiscing elit, sed do eiusmod tempor incididunt ut labore et dolore magna aliqua. Quis ipsum suspendisse ultrices gravida. Risus commodo viverra maecenas accumsan lacus vel facilisis. Lorem ipsum dolor sit amet, consectetur adipiscing elit, sed do eiusmod tempor incididunt ut labore et dolore magna aliqua. Quis ipsum suspendisse ultrices gravida. Risus commodo viverra maecenas accumsan lacus vel facilisis. Lorem ipsum dolor sit amet, consectetur adipiscing elit, sed do eiusmod tempor incididunt ut labore et dolore magna aliqua. Quis ipsum suspendisse ultrices gravida. Risus commodo viverra maecenas accumsan lacus vel facilisis. Lorem ipsum dolor sit amet, consectetur adipiscing elit, sed do eiusmod tempor incididunt ut labore et dolore magna aliqua. Quis ipsum suspendisse ultrices gravida. Risus commodo viverra maecenas accumsan lacus vel facilisis.</p>
      <p class="blurb">Lorem ipsum dolor sit amet, consectetur adipiscing elit, sed do eiusmod tempor incididunt ut labore et dolore magna aliqua. Quis ipsum suspendisse ultrices gravida. Risus commodo viverra maecenas accumsan lacus vel facilisis. Lorem ipsum dolor sit amet, consectetur adipiscing elit, sed do eiusmod tempor incididunt ut labore et dolore magna aliqua. Quis ipsum suspendisse ultrices gravida. Risus commodo viverra maecenas accumsan lacus vel facilisis.</p>
    </section>

    <section class="spine">
      <svg class="spine-text" viewBox="0 0 45 790" aria-label="Quiet Under Glass, Bastien Marchetaud, Editions Brunelle">
        <g transform="rotate(90)">
          <text class="spine-title" x="44" y="-11" fill="var(--ink-light)" textLength="258" lengthAdjust="spacingAndGlyphs">QUIET UNDER</text>
          <text class="spine-title" x="314" y="-11" fill="var(--accent-red)" textLength="84" lengthAdjust="spacingAndGlyphs">GLASS</text>
          <text class="spine-author" x="420" y="-16" fill="var(--ink-light)" textLength="226" lengthAdjust="spacingAndGlyphs">BASTIEN MARCHETAUD</text>
          <text class="spine-publisher" x="668" y="-19" fill="var(--ink-light)" textLength="102" lengthAdjust="spacingAndGlyphs">EDITIONS BRUNELLE</text>
        </g>
      </svg>
    </section>

    <section class="front-cover">
      <div class="cover-photo" role="img" aria-label="Photograph of a long dim hospital corridor with a bright light at its end and a lone silhouetted figure walking toward the viewer"></div>
      <svg class="front-title" viewBox="0 0 527 640" aria-label="Quiet Under Glass">
        <text x="52" y="300" fill="var(--ink-light)" textLength="424" lengthAdjust="spacingAndGlyphs">QUIET</text>
        <text x="42" y="448" fill="var(--ink-light)" textLength="444" lengthAdjust="spacingAndGlyphs">UNDER</text>
        <text x="54" y="596" fill="var(--accent-red)" textLength="420" lengthAdjust="spacingAndGlyphs">GLASS</text>
      </svg>
      <p class="author">Bastien Marchetaud</p>
      <p class="publisher">Editions Brunelle</p>
    </section>
  </main>
</body>
</html>
```